Hip / Cool Business Card for Custom Accessory Company

I would like to get a 2 sided design for standard size business cards, glossy (2 inches x 3.5 inches). Can be landscape or portrait layout! The design should include our logo (attached). The card should be extremely clear that the company is Tin Lantern. Should also have our URL clear. Should also use the color scheme seen on our upcoming site, tinlantern-example.com. The font we use is called "hurry up." Other than that, please go-to-town. We are targeting 15-45 y.o. market, with a skew on the 20-30 crowd. We do custom and stock iPhone cases as well as Cufflinks, Winestoppers; see the website for more.
Updates

Project Deadline Extended
Reason: Extending in case the US July 4th Holiday is keeping people from working!!

Industry/Entity Type

Landscape

Requirements
Must have
• Must be clear that the website is tinlantern-example.com. Must be clear that custom designs are an option.
Nice to have
• images of our designs. examples of our designs.
Should not have
• hard on the eyes contrasting colors such as orange on black. green on blue. Should not have any fonts that are considered "old" like Times New Roman. But decorative fonts are fine.

```html
<!DOCTYPE html>
<html lang="en">
<head>
<meta charset="utf-8">
<title>Tin Lantern — Business Card</title>
<link rel="stylesheet" href="https://fonts.googleapis.com/css2?family=Orbitron:wght@500;800&family=Cinzel:wght@400;600&display=swap">
<style>
  :root {
    --page: #eceae6;
    --white: #ffffff;
    --ink: #333438;
    --black: #111214;
    --red: #9e1b1f;
    --navy: #0e3a66;
    --navy-deep: #0a2c52;
    --teal-glow: #3cc3c9;
    --teal: #1d9aa6;
    --teal-deep: #0f5f86;
    --mark: #2aa7ad;
    --role: #3a7fb0;
  }
  * { box-sizing: border-box; margin: 0; padding: 0; }
  html, body { width: 1200px; height: 739px; overflow: hidden; background: var(--page); }
  .sheet {
    position: relative; width: 1200px; height: 739px;
    display: flex; align-items: center; justify-content: center; gap: 40px;
  }
  .card {
    position: relative; width: 540px; height: 309px; overflow: hidden;
    box-shadow: 0 6px 18px rgba(0,0,0,.18);
  }

  /* Front side */
  .card-front { background: var(--white); }
  .brand {
    position: absolute; left: 44px; top: 48px;
    display: flex; align-items: center; gap: 16px;
  }
  .brand-dot { width: 78px; height: 78px; border-radius: 50%; background: var(--mark); }
  .brand-name {
    font-family: "Orbitron", sans-serif; font-weight: 500;
    font-size: 38px; letter-spacing: 2px; color: var(--ink); white-space: nowrap;
  }
  .person {
    position: absolute; left: 118px; top: 140px;
    font-family: "Cinzel", serif; font-size: 15px; white-space: nowrap;
  }
  .person-name { color: var(--red); font-weight: 600; }
  .person-role { color: var(--role); margin-left: 12px; font-size: 13px; }
  .rule-red { position: absolute; left: 0; right: 0; top: 164px; height: 2px; background: var(--red); }
  .front-band {
    position: absolute; left: 0; right: 0; top: 170px; bottom: 0;
    background: linear-gradient(90deg, #2d5f8f 0%, var(--navy) 45%, var(--navy-deep) 100%);
  }
  .address {
    position: absolute; left: 80px; top: 200px; width: 206px; text-align: right;
    font-family: "Cinzel", serif; font-size: 12px; line-height: 18px; color: #e6eef6;
  }
  .divider { position: absolute; left: 300px; top: 180px; width: 1px; height: 78px; background: rgba(255,255,255,.35); }
  .contacts {
    position: absolute; left: 312px; top: 184px; list-style: none;
    font-family: "Cinzel", serif; font-size: 10px; line-height: 17px; color: var(--white);
  }
  .contacts li { display: flex; align-items: center; gap: 6px; white-space: nowrap; }
  .contacts svg { width: 10px; height: 10px; flex: none; }

  /* Back side */
  .card-back {
    background: radial-gradient(ellipse 62% 78% at 50% 52%, var(--teal-glow) 0%, var(--teal) 40%, var(--teal-deep) 72%, var(--navy-deep) 100%);
    display: flex; align-items: center; justify-content: center;
  }
  .back-brand { display: flex; flex-direction: column; align-items: center; gap: 10px; }
  .back-dot { width: 104px; height: 104px; border-radius: 50%; background: var(--mark); }
  .back-word {
    font-family: "Orbitron", sans-serif; font-weight: 800;
    font-size: 34px; letter-spacing: 3px; color: var(--black); line-height: 1;
  }
</style>
</head>
<body>
<main class="sheet">
  <section class="card card-front" aria-label="Card front">
    <div class="brand">
      <span class="brand-dot"></span>
      <span class="brand-name">TIN LANTERN</span>
    </div>
    <p class="person"><span class="person-name">Dana Whitfield</span><span class="person-role">Custom Design Consultant</span></p>
    <div class="rule-red"></div>
    <div class="front-band"></div>
    <p class="address">48 Harbour Lane ,<br>Melbourne</p>
    <div class="divider"></div>
    <ul class="contacts">
      <li><svg viewBox="0 0 10 10"><circle cx="5" cy="5" r="5" fill="#c0392b"/><path d="M3 2.5l1 1-.6.8a4 4 0 0 0 2.3 2.3l.8-.6 1 1-.7.9C4.8 7.6 2.4 5.2 2.1 3.2z" fill="#fff"/></svg>07700 900 123</li>
      <li><svg viewBox="0 0 10 10"><circle cx="5" cy="5" r="5" fill="#c0392b"/><path d="M3 2.5l1 1-.6.8a4 4 0 0 0 2.3 2.3l.8-.6 1 1-.7.9C4.8 7.6 2.4 5.2 2.1 3.2z" fill="#fff"/></svg>0117 496 0170</li>
      <li><svg viewBox="0 0 10 10"><circle cx="5" cy="5" r="5" fill="#c0392b"/><rect x="2.3" y="3" width="5.4" height="4" fill="none" stroke="#fff" stroke-width=".8"/><path d="M2.3 3l2.7 2 2.7-2" fill="none" stroke="#fff" stroke-width=".8"/></svg>info@tinlantern-example.com</li>
      <li><svg viewBox="0 0 10 10"><circle cx="5" cy="5" r="5" fill="#c0392b"/><circle cx="5" cy="5" r="2.6" fill="none" stroke="#fff" stroke-width=".8"/><path d="M2.4 5h5.2M5 2.4v5.2" stroke="#fff" stroke-width=".6"/></svg>www.tinlantern-example.com</li>
    </ul>
  </section>

  <section class="card card-back" aria-label="Card back">
    <div class="back-brand">
      <span class="back-word">TIN</span>
      <span class="back-dot"></span>
      <span class="back-word">LANTERN</span>
    </div>
  </section>
</main>
</body>
</html>
```